Wealth management firm needs a business card design

Using my logo, create a business card that covers all of the regulatory wordings that I need. It must have - Registered Office 7-9 Pelgrove Wynd, Edinburgh, EH4 2QN. Registered in Scotland under number SC804317. VORELT Wealth Management Ltd is an appointed representative of Kestoby wealth management Ltd, which is authorised and regulated by the Monetary Oversight Council.

Target Market(s)

professional clients

Industry/Entity Type

finance

Contact Information for Business Card

VORELT Wealth Management, Conor Tresk-Whitlaw, Director, 5 Dunmore Row, Edinburgh, EH9 4RT. 07812 459 163, conor.tresk-whitlaw@vorelt-example.com , www.vorelt-example.com

Font styles to use
Serif

Colors
0054AA
0677BA
7BADD7
CADEEF
E8F1F8

Requirements
Must have
• regulatory wording in small text at bottom

```html
<!DOCTYPE html>
<html lang="en">
<head>
<meta charset="utf-8">
<title>VORELT Wealth Management – Business Card</title>
<link href="https://fonts.googleapis.com/css2?family=Noto+Serif:wght@400;500&family=Tinos&family=Mulish:wght@400;800&display=swap" rel="stylesheet">
<style>
  :root {
    --page: #c4c5c7;
    --card: #f4f4f5;
    --card-edge: #e2e3e5;
    --ink: #1c1c28;
    --brand: #2f62b0;
    --brand-dot: #3b6db5;
    --text: #2a2a2e;
  }
  * { margin: 0; padding: 0; box-sizing: border-box; }
  html, body {
    width: 900px; height: 1200px; overflow: hidden;
    background: var(--page);
  }
  .card {
    position: absolute; left: 149px; width: 602px; height: 386px;
    background: radial-gradient(ellipse at 55% 45%, #ffffff 0%, var(--card) 55%, var(--card-edge) 100%);
  }
  .card--front { top: 200px; }
  .card--back { top: 613px; }

  /* Front */
  .front__mark {
    position: absolute; left: 50%; top: 123px; width: 84px; height: 84px;
    margin-left: -42px; border-radius: 50%; background: var(--brand-dot);
  }
  .front__name {
    position: absolute; left: 0; right: 0; top: 218px; text-align: center;
    font-family: "Noto Serif", serif; font-size: 30px; font-weight: 400;
    color: var(--ink); letter-spacing: 0.2px;
  }
  .front__tagline {
    position: absolute; left: 0; right: 0; top: 258px; text-align: center;
    font-family: "Noto Serif", serif; font-size: 11.5px; color: var(--ink);
  }
  .front__legal {
    position: absolute; left: 30px; right: 30px; top: 330px; text-align: center;
    font-family: "Tinos", serif; font-size: 8.6px; line-height: 15px; color: var(--ink);
  }

  /* Back */
  .back__name {
    position: absolute; left: 38px; top: 48px;
    font-family: "Mulish", sans-serif; font-weight: 800; font-size: 25px;
    color: var(--brand); letter-spacing: 0.2px;
  }
  .back__role {
    position: absolute; left: 38px; top: 77px;
    font-family: "Mulish", sans-serif; font-size: 16px; color: var(--text); letter-spacing: 0.8px;
  }
  .back__address {
    position: absolute; left: 38px; top: 196px;
    font-family: "Mulish", sans-serif; font-size: 16.5px; line-height: 25px;
    color: var(--text); letter-spacing: 0.8px;
  }
  .back__contacts {
    position: absolute; left: 38px; top: 268px; list-style: none;
    font-family: "Mulish", sans-serif; font-size: 16.5px; color: var(--text); letter-spacing: 0.9px;
  }
  .back__contacts li { display: flex; align-items: center; height: 23.5px; }
  .back__contacts svg { width: 13px; height: 13px; margin-right: 10px; fill: var(--brand); flex: none; }
  .back__brand {
    position: absolute; left: 352px; top: 110px; width: 200px; text-align: center;
  }
  .back__brand-dot {
    width: 110px; height: 110px; border-radius: 50%; background: var(--brand-dot);
    margin: 0 auto 14px;
  }
  .back__brand-name {
    font-family: "Mulish", sans-serif; font-weight: 800; font-size: 24px;
    color: var(--brand); letter-spacing: 3px;
  }
</style>
</head>
<body>
  <section class="card card--front">
    <div class="front__mark"></div>
    <h1 class="front__name">VORELT Wealth Management Ltd</h1>
    <p class="front__tagline">Personal Financial Advice</p>
    <p class="front__legal">Registered Office 7-9 Pelgrove Wynd, Edinburgh, EH4 2QN. Registered in Scotland under number SC804317. VORELT Wealth Management Ltd is an appointed representative of Kestoby wealth management Ltd, which is authorised and regulated by the Monetary Oversight Council.</p>
  </section>

  <section class="card card--back">
    <h2 class="back__name">Conor Tresk-Whitlaw</h2>
    <p class="back__role">Director</p>
    <p class="back__address">5 Dunmore Row,<br>Edinburgh, EH9 4RT.</p>
    <ul class="back__contacts">
      <li><svg viewBox="0 0 24 24"><path d="M6.6 10.8a15.1 15.1 0 0 0 6.6 6.6l2.2-2.2a1 1 0 0 1 1-.25 11.4 11.4 0 0 0 3.6.57 1 1 0 0 1 1 1V20a1 1 0 0 1-1 1A17 17 0 0 1 3 4a1 1 0 0 1 1-1h3.5a1 1 0 0 1 1 1c0 1.25.2 2.45.57 3.57a1 1 0 0 1-.25 1z"/></svg>07812 459 163</li>
      <li><svg viewBox="0 0 24 24"><path d="M12 2a10 10 0 1 0 0 20 10 10 0 0 0 0-20zm6.9 6h-3a15.6 15.6 0 0 0-1.4-3.6A8 8 0 0 1 18.9 8zM12 4c.8 1.2 1.5 2.5 1.9 4h-3.8c.4-1.5 1.1-2.8 1.9-4zM4.3 14a8 8 0 0 1 0-4h3.4a16 16 0 0 0 0 4zm.8 2h3a15.6 15.6 0 0 0 1.4 3.6A8 8 0 0 1 5.1 16zm3-8h-3a8 8 0 0 1 4.4-3.6A15.6 15.6 0 0 0 8.1 8zM12 20c-.8-1.2-1.5-2.5-1.9-4h3.8c-.4 1.5-1.1 2.8-1.9 4zm2.3-6H9.7a14.7 14.7 0 0 1 0-4h4.6a14.7 14.7 0 0 1 0 4zm.2 5.6a15.6 15.6 0 0 0 1.4-3.6h3a8 8 0 0 1-4.4 3.6zm1.8-5.6a16 16 0 0 0 0-4h3.4a8 8 0 0 1 0 4z"/></svg>www.vorelt-example.com</li>
      <li><svg viewBox="0 0 24 24"><path d="M2 5h20v14H2zm2 2v.5l8 5 8-5V7zm0 2.8V17h16V9.8l-8 5z"/></svg>conor.tresk-whitlaw@vorelt-example.com</li>
    </ul>
    <div class="back__brand">
      <div class="back__brand-dot"></div>
      <p class="back__brand-name">VORELT</p>
    </div>
  </section>
</body>
</html>
```